“Good Dog” fun and creative design sought for photo frame!

Seeking 8x10 inch photo frame with opening for dog’s photo. Dimensions must fit exact measurement specs of sample layout templates. Choose any of the three layout templates (labeled "Template 1," "Template 2" and "Template 3"). Our customers will upload their own dog’s photo to the frame and be able to print them out at 8 inches by 10 inches. The location of the opening for the dog’s photo must match one of the templates precisely. The opening for the dog's photo must have the EXACT same measurements as the templates - it cannot be round or any other shape - it must match the templates exactly. Samples of other Maple Nook Prints are posted just to give you a general idea of what some other designs look like from other designers. The text on the frame for this job should say “Good Dog.” Feel free to use the paw print PSD, but not required. Of course, no copyrighted materials should be used in the design.
Dog lovers
Seeking

```html
<!DOCTYPE html>
<html lang="en">
<head>
<meta charset="utf-8">
<title>Good Dog Photo Frame</title>
<link rel="stylesheet" href="https://fonts.googleapis.com/css2?family=Cinzel:wght@500;600&display=swap">
<style>
  :root {
    --stage: #d9d9d9;
    --sun-yellow: #f6ea3a;
    --pale-yellow: #fbf6b8;
    --leaf-green: #b9d77a;
    --orchid: #c04ea8;
    --lilac: #b79ad8;
    --sky-blue: #7f9fd6;
    --mist: #f4f6fb;
    --gold-light: #fff6d8;
    --gold-mid: #e3c27a;
    --gold-deep: #9c7436;
    --gold-edge: #5b4216;
    --coat-dark: #1d1a1c;
    --coat-tan: #a8733c;
  }
  * { margin: 0; padding: 0; box-sizing: border-box; }
  html, body {
    width: 1200px;
    height: 1200px;
    overflow: hidden;
    background: var(--stage);
  }
  .frame {
    position: absolute;
    left: 149px;
    top: 72px;
    width: 902px;
    height: 1056px;
    overflow: hidden;
    background:
      radial-gradient(circle at 45% 48%, rgba(255,255,255,0.85) 0%, rgba(255,255,255,0) 38%),
      linear-gradient(180deg,
        var(--sun-yellow) 0%,
        var(--pale-yellow) 28%,
        var(--leaf-green) 42%,
        var(--lilac) 58%,
        var(--mist) 74%,
        var(--sky-blue) 100%);
  }
  .light-rays {
    position: absolute;
    inset: 0;
    width: 100%;
    height: 100%;
  }
  .splash-art {
    position: absolute;
    left: 80px;
    top: 210px;
    width: 760px;
    height: 600px;
    border-radius: 50%;
    background:
      radial-gradient(ellipse at 50% 55%,
        rgba(192,78,168,0.75) 0%,
        rgba(183,154,216,0.55) 40%,
        rgba(127,159,214,0.25) 65%,
        rgba(255,255,255,0) 78%);
  }
  .photo-opening {
    position: absolute;
    left: 255px;
    top: 321px;
    width: 446px;
    height: 380px;
    background: linear-gradient(180deg, var(--coat-dark) 0%, #2b2428 55%, var(--coat-tan) 100%);
  }
  .headline {
    position: absolute;
    left: 0;
    width: 100%;
    text-align: center;
    font-family: "Cinzel", "Times New Roman", serif;
    font-weight: 600;
    font-size: 160px;
    line-height: 1;
    background: linear-gradient(180deg,
      var(--gold-light) 0%,
      var(--gold-mid) 40%,
      var(--gold-deep) 62%,
      var(--gold-light) 85%,
      var(--gold-mid) 100%);
    -webkit-background-clip: text;
    background-clip: text;
    color: transparent;
    filter: drop-shadow(3px 4px 0 var(--gold-edge)) drop-shadow(0 6px 8px rgba(0,0,0,0.25));
  }
  .headline--top { top: 66px; padding-left: 38px; }
  .headline--bottom { top: 776px; }
</style>
</head>
<body>
  <main class="frame">
    <svg class="light-rays" viewBox="0 0 902 1056" aria-hidden="true">
      <g fill="#ffffff" opacity="0.28">
        <polygon points="451,480 120,0 250,0"/>
        <polygon points="451,480 560,0 700,0"/>
        <polygon points="451,480 902,120 902,260"/>
        <polygon points="451,480 902,560 902,700"/>
        <polygon points="451,480 760,1056 620,1056"/>
        <polygon points="451,480 260,1056 130,1056"/>
        <polygon points="451,480 0,820 0,700"/>
        <polygon points="451,480 0,380 0,260"/>
      </g>
      <g fill="#ffffff" opacity="0.35">
        <circle cx="170" cy="60" r="38"/>
        <circle cx="640" cy="30" r="30"/>
        <circle cx="60" cy="200" r="26"/>
        <circle cx="840" cy="170" r="34"/>
        <circle cx="110" cy="620" r="30"/>
        <circle cx="820" cy="880" r="40"/>
        <circle cx="40" cy="980" r="34"/>
      </g>
      <g fill="#ffffff" opacity="0.8">
        <circle cx="690" cy="701" r="3"/><circle cx="710" cy="701" r="3"/>
        <circle cx="730" cy="701" r="3"/><circle cx="750" cy="701" r="3"/>
        <circle cx="770" cy="701" r="3"/><circle cx="790" cy="701" r="3"/>
      </g>
    </svg>
    <div class="splash-art" role="img" aria-label="Decorative paint splash in violet, magenta and blue behind the photo"></div>
    <div class="photo-opening" role="img" aria-label="Rectangular opening for the customer's dog photo"></div>
    <h1 class="headline headline--top">GOOD</h1>
    <p class="headline headline--bottom">DOG</p>
  </main>
</body>
</html>
```